Landing Page IT Security Vendor

We need a landing page that uses our colour scheme (www.veldonguard.com). We created a draft (see attached). We do not need standard stock template design pages. Please only apply if you can design pages from scratch and try to be as close as possible to our draft. It is ok to also purchase commecrial stock pictures

Coding

Coded - Design and coding required

Number of Pages Required

1 page

```html
<!DOCTYPE html>
<html lang="en">
<head>
<meta charset="utf-8">
<title>Veldon Guard – Security Awareness Training</title>
<link href="https://fonts.googleapis.com/css2?family=Figtree:wght@400;500;600;700;800&display=swap" rel="stylesheet">
<style>
:root{
  --teal:#00b2bd;
  --teal-light:#b9e9ec;
  --orange:#f7a21b;
  --orange-dark:#ec7a23;
  --ink:#2e2e2e;
  --band:#383838;
  --white:#fff;
}
*{box-sizing:border-box;margin:0;padding:0}
html,body{width:1200px;height:2406px;overflow:hidden}
body{font-family:"Figtree",sans-serif;background:var(--white);color:var(--ink);position:relative}
.abs{position:absolute}
.hero{position:absolute;left:0;top:0;width:1200px;height:1364px;background:var(--teal)}
.topbar{left:58px;top:32px;width:1083px;height:50px;border-radius:25px;background:rgba(255,255,255,.1);display:flex;align-items:center;padding:0 16px;gap:18px}
.award{display:flex;align-items:center;gap:12px;color:#fff;font-size:10px;font-weight:600;line-height:1.6;width:290px}
.award svg{flex:none}
.nav-home{margin-left:6px;background:rgba(255,255,255,.35);color:#fff;font-size:14px;border-radius:18px;padding:8px 18px}
.nav-sol{color:#fff;font-size:14px;font-weight:600;margin-left:6px}
.hero-photo{left:820px;top:140px;width:380px;height:700px;border-radius:190px 0 0 60px;background:linear-gradient(160deg,#3fc4cc 0%,#8fd9dd 55%,#e9f5f6 100%)}
.kicker{left:58px;top:224px;color:#fff;font-size:28px;font-weight:500;letter-spacing:.2px}
.headline{left:58px;top:285px;width:640px;color:#fff;font-size:47px;font-weight:800;line-height:60px}
.demo{left:58px;top:512px;width:291px;height:74px;border-radius:37px;background:var(--teal-light);color:#3a8f96;font-size:24px;letter-spacing:1.5px;display:flex;align-items:center;justify-content:center}
.help{left:204px;top:740px;color:#fff;font-size:35px;font-weight:800}
.card{top:857px;width:326px;height:395px;background:#fff;border-radius:12px;padding:33px 34px}
.card h3{color:var(--orange);font-size:19px;font-weight:800;line-height:24px;text-transform:uppercase;height:56px}
.card .lead{font-size:15.5px;font-weight:600;line-height:20px;margin-top:8px}
.card .body{font-size:15.5px;line-height:20px;margin-top:20px;height:80px;overflow:hidden}
.btn{display:flex;align-items:center;justify-content:center;border-radius:6px;background:linear-gradient(90deg,var(--orange),var(--orange-dark));color:#fff;font-weight:700;letter-spacing:1px;font-size:14px;box-shadow:0 6px 14px rgba(0,0,0,.12)}
.card .btn{position:absolute;left:34px;bottom:39px;width:258px;height:55px}
.band{left:0;top:1364px;width:1200px;height:98px;background:var(--band);color:#fff;font-size:26px;font-weight:700;display:flex;align-items:center;justify-content:center;gap:8px}
.band a{color:#fff}
.trust-h{left:58px;top:1556px;font-size:33px;font-weight:700;line-height:42px;width:520px}
.trust-h em{font-style:normal;color:var(--orange)}
.trust-p{left:58px;top:1700px;width:540px;font-size:15.5px;line-height:20px;color:#444}
.trust-p p{margin-bottom:12px}
.cta{left:58px;top:1865px;width:584px;height:60px;font-size:14px}
.client{font-weight:800;font-size:22px;display:flex;align-items:center;justify-content:center;height:86px}
.footer{left:0;top:2025px;width:1200px;height:381px;background:var(--teal);color:#fff}
.footer h4{position:absolute;font-size:17px;font-weight:800}
.footer .col{position:absolute;font-size:14px;font-weight:500;line-height:21px}
.rule{left:58px;top:2290px;width:1085px;height:1px;background:rgba(255,255,255,.6)}
.badge{position:absolute;top:2318px;width:62px;height:62px;background:rgba(255,255,255,.25)}
</style>
</head>
<body>
<section class="hero">
  <div class="abs hero-photo" role="img" aria-label="Smiling woman holding a coffee cup and a laptop, with white line-drawn office doodles around her"></div>
  <div class="abs topbar">
    <div class="award"><svg width="30" height="30" viewBox="0 0 30 30"><path d="M8 4h14v7a7 7 0 0 1-14 0z M4 6h4v4a4 4 0 0 1-4-4z M22 6h4a4 4 0 0 1-4 4z M13 18h4v5h-4z M9 24h12v3H9z" fill="#fff"/></svg>In 2020, VELDON won the Cyber Security Excellence Award for Best "Anti Phishing"</div>
    <div class="award"><svg width="34" height="34" viewBox="0 0 34 34"><circle cx="17" cy="17" r="11" fill="none" stroke="#fff" stroke-width="2"/><path d="M17 10l2 5h5l-4 3 2 5-5-3-5 3 2-5-4-3h5z" fill="#fff"/></svg>In 2020, VELDON won the Cyber Security Excellence Award for Best "Security Education Platform".</div>
    <div class="award"><svg width="34" height="34" viewBox="0 0 34 34"><circle cx="17" cy="17" r="12" fill="none" stroke="#fff" stroke-width="2"/><text x="17" y="22" text-anchor="middle" fill="#fff" font-size="14" font-weight="700" font-family="Figtree,sans-serif">1</text></svg>2020 Gold Winner "Cyber Security Education and Training" in the Security Product Digest</div>
    <span class="nav-home">Home</span><span class="nav-sol">Sulutions ⌄</span>
  </div>
  <div class="abs kicker">CYBER SERCURITY STARTS WITH PEOPLE</div>
  <h1 class="abs headline">TRAIN YOUR STAFF WITH VELDON AND IMPROVE CYBER SERCURITY AWARENESS</h1>
  <div class="abs demo">Request a demo</div>
  <h2 class="abs help">HOW CAN WE HELP</h2>
  <svg class="abs" style="left:204px;top:806px" width="800" height="36"><path d="M2 34V3H796V34M402 3V34" fill="none" stroke="#fff" stroke-width="3" stroke-dasharray="7 5"/></svg>
  <div class="abs card" style="left:58px"><h3>Import our training courses in your LMS</h3><p class="lead">Buy out of the box or custom tailored security courses you can import in your elearning (SCORM)</p><p class="body">VELDON offers 250 fully customizable training modules in +30 languages. Games, videos, exarms, posters, offline, micro-training and much</p><div class="btn">EXPLORE OUR TRAINING</div></div>
  <div class="abs card" style="left:437px"><h3>Let us develop a security awareness</h3><p class="lead">VELDON Security will assist you in improving security awareness with money back guarantee!</p><p class="body">Our security awareness specialists will identify risky users via phishing simulations. We develop a tailored awareness program and reduce</p><div class="btn">EXPLORE OUR SERVICES</div></div>
  <div class="abs card" style="left:815px"><h3>Install the VELDON software on-premise</h3><p class="lead">You want to run the campaign yourself? Choose your preferred setup type and get started in 24h!</p><p class="body">The VELDON software can be installed on-premise or in the cloud. If you don't want to deal with the installation we onboard you in</p><div class="btn">EXPLORE OUR SOFTWARE</div></div>
</section>
<div class="abs band">VELDON is also available for MSSP - <a href="#">learn more</a></div>
<h2 class="abs trust-h">Already over <em>12'000'000</em> Employees worldwide trust and use VELDON.</h2>
<div class="abs trust-p"><p>Veldon Guard is a name you can trust! Because we have won countless awards since 2015 and help well-known brands around the world.</p><p>You know you're gettinga quality solution with usS.</p><p>Our services can be customized to fit your needs and company size. Talk to our team today to learn more.</p></div>
<div class="abs btn cta">GET IN CONTACT WITH THE VELDON TEAM NOW!</div>
<div class="abs client" style="left:731px;top:1554px;width:82px;color:#1d2c8c">Arvex</div>
<div class="abs client" style="left:852px;top:1554px;width:121px;color:#e2001a">NordRail</div>
<div class="abs client" style="left:1008px;top:1554px;width:120px;color:#e30613;font-size:18px">Mobilia Mutual</div>
<div class="abs client" style="left:731px;top:1670px;width:155px;color:#e20015">Kessler Tech</div>
<div class="abs client" style="left:910px;top:1670px;width:222px;color:#0a1f7a">Altair Aero</div>
<div class="abs client" style="left:731px;top:1767px;width:182px;color:#008b8f">Brenner</div>
<div class="abs client" style="left:944px;top:1767px;width:186px;color:#3e5aa8;font-weight:500">Vantor Informatik</div>
<div class="abs client" style="left:731px;top:1857px;width:186px;color:#222">Solvane</div>
<div class="abs client" style="left:944px;top:1857px;width:190px;color:#444;font-weight:500;font-size:18px">Stadtwerk Nordhafen</div>
<footer class="abs footer">
  <h4 style="left:58px;top:68px">CONTACTS</h4>
  <h4 style="left:1000px;top:68px">LANGUAGE</h4>
  <div class="col" style="left:58px;top:102px">Address: Europe<br>Veldon Guard AG<br>Lindenweg 12 | 6340 Baar | Switzerland</div>
  <div class="col" style="left:421px;top:102px">Address: North America<br>Veldon Guard USA<br>4820 Harbor Lane<br>Suite 210<br>Denver, CO 80202</div>
  <div class="col" style="left:703px;top:102px">Phone Global: +41 44 000 12 34<br>Phone USA: +1-555-010-2200<br>Phone USA Support: +1-555-010-2214<br>Phone France: +33 600 000 111<br>Phone UK: +44 (0) 7000 555010</div>
  <div class="col" style="left:1000px;top:102px">English ⌄</div>
  <div class="col" style="left:58px;top:290px;font-size:16px;font-weight:800;display:flex;align-items:center;gap:6px"><span style="width:16px;height:16px;border-radius:50%;background:#f7a21b;display:inline-block"></span>Veldon</div>
  <div class="col" style="left:58px;top:316px">All Rights Reserved 2020</div>
</footer>
<div class="abs rule"></div>
<div class="badge" style="left:322px"></div>
<div class="badge" style="left:412px;border-radius:50%"></div>
<div class="badge" style="left:498px"></div>
<div class="badge" style="left:567px"></div>
<div class="badge" style="left:637px"></div>
<div class="badge" style="left:710px"></div>
<div class="badge" style="left:797px"></div>
<div class="badge" style="left:870px"></div>
<div class="badge" style="left:960px;width:92px;height:40px;top:2329px;border-radius:20px"></div>
<div class="badge" style="left:1076px;border-radius:50%"></div>
</body>
</html>
```